Business Card for Amber Heron Advisors

Business card design for Amber Heron Advisors, a new consulting and financial advisory firm. I would like the designs to integrate the logo attached (at least on 1 side).

Target Market(s)

individual and institutional clients

Contact Information for Business Card

Dominic L. Hartwell, CFA
Managing Director
amberheronadvisors.examplep
hartwell@amberheronadvisors.example
(555) 218-4903

```html
<!DOCTYPE html>
<html lang="en">
<head>
<meta charset="utf-8">
<title>Amber Heron Advisors – Business Card</title>
<link rel="stylesheet" href="https://fonts.googleapis.com/css2?family=Lato:wght@400;700&family=Raleway:wght@500;700&display=swap">
<style>
  :root {
    --backdrop: #ececec;
    --card-dark: #282828;
    --card-light: #ffffff;
    --amber: #e27f26;
    --ink: #1d1d1d;
    --band-grey: #a3a3a3;
  }
  * { box-sizing: border-box; margin: 0; padding: 0; }
  html, body {
    width: 1200px; height: 586px; overflow: hidden;
    background: var(--backdrop);
  }
  .stage { position: relative; width: 1200px; height: 586px; }
  .card {
    position: absolute; top: 143px; width: 502px; height: 300px; overflow: hidden;
  }
  .card--front { left: 65px; background: var(--card-dark); }
  .card--back  { left: 608px; background: var(--card-light); }

  .wordmark {
    font-family: "Lato", sans-serif; font-weight: 700; color: var(--amber);
    letter-spacing: 0.5px; white-space: nowrap;
  }
  .card--front .wordmark {
    position: absolute; left: 0; right: 0; top: 126px;
    text-align: center; font-size: 36px; line-height: 48px;
  }
  .card--back .wordmark {
    position: absolute; left: 0; right: 0; top: 50px;
    text-align: center; font-size: 22px; line-height: 30px;
  }

  .contact {
    position: absolute; left: 28px; top: 203px;
    font-family: "Lato", sans-serif; font-size: 12px; font-weight: 700; color: var(--ink);
  }
  .contact__row { display: flex; align-items: center; height: 24px; }
  .contact__icon { width: 13px; height: 13px; margin-right: 8px; flex: none; }
  .contact__address { color: var(--amber); font-size: 12.5px; margin-top: 2px; }

  .person {
    position: absolute; right: 28px; top: 220px; text-align: right;
  }
  .person__name {
    font-family: "Raleway", sans-serif; font-weight: 700; font-size: 16px;
    color: var(--amber); line-height: 20px;
  }
  .person__title {
    font-family: "Lato", sans-serif; font-weight: 400; font-size: 11px;
    color: var(--ink); margin-top: 2px;
  }
  .card__bands { position: absolute; left: 0; bottom: 0; width: 502px; height: 15px; }
</style>
</head>
<body>
<main class="stage">
  <section class="card card--front" aria-label="Card front">
    <p class="wordmark">Amber Heron Advisors</p>
  </section>

  <section class="card card--back" aria-label="Card back">
    <p class="wordmark">Amber Heron Advisors</p>

    <div class="contact">
      <div class="contact__row">
        <svg class="contact__icon" viewBox="0 0 16 16" aria-hidden="true">
          <path fill="#e27f26" d="M1 5c0-2 3-3 7-3s7 1 7 3v1.5h-3.5V5h-7v1.5H1z M3 8h10l1.5 6h-13z"/>
          <circle cx="8" cy="10.8" r="1.8" fill="#fff"/>
        </svg>
        <span>(555) 218-4903</span>
      </div>
      <div class="contact__row">
        <svg class="contact__icon" viewBox="0 0 16 16" aria-hidden="true">
          <rect x="1" y="3" width="14" height="10" fill="#e27f26"/>
          <path d="M1.5 3.5 8 9l6.5-5.5" fill="none" stroke="#fff" stroke-width="1.2"/>
        </svg>
        <span>hartwell@amberheronadvisors.example</span>
      </div>
      <div class="contact__address">P.O. Box 40518, Fairhaven, 10000</div>
    </div>

    <div class="person">
      <p class="person__name">Dominic L. Hartwell, CFA</p>
      <p class="person__title">Managing Director</p>
    </div>

    <svg class="card__bands" viewBox="0 0 502 15" preserveAspectRatio="none" aria-hidden="true">
      <rect x="0" y="2" width="310" height="13" fill="var(--band-grey)"/>
      <path d="M296 15 Q300 2 318 1 H502 V15 Z" fill="#fff"/>
      <path d="M302 15 Q306 0 322 0 H502 V15 Z" fill="var(--amber)"/>
    </svg>
  </section>
</main>
</body>
</html>
```